Velmora - New coded website

Current website is around 5 years old and corrupted in some ways...
I would like to refresh the design and to create a new coded website based on the current content .
Please refer to :
www.velmora-sample.com.au

Coded - Design and coding required

```html
<!DOCTYPE html>
<html lang="en">
<head>
<meta charset="utf-8">
<title>Velmora – Odours Controlled Naturally</title>
<link href="https://fonts.googleapis.com/css2?family=Poppins:wght@300;400;500;600;700&family=Allura&display=swap" rel="stylesheet">
<style>
:root{
  --green:#5cb335;
  --green-dark:#3f8f1f;
  --green-soft:#e8f3df;
  --navy:#0f2c3d;
  --navy-deep:#0a2130;
  --ink:#2b3540;
  --muted:#6f7a84;
  --line:#dfe6df;
  --white:#ffffff;
}
*{box-sizing:border-box;margin:0;padding:0}
html,body{width:1200px;height:4648px;overflow:hidden}
body{font-family:"Poppins",sans-serif;color:var(--ink);background:var(--white);position:relative}
section,header,footer{position:relative;width:1200px;overflow:hidden}
.script{font-family:"Allura",cursive;color:var(--green);font-size:34px;line-height:1}
.btn{display:inline-block;background:var(--green);color:var(--white);font-size:12px;font-weight:600;letter-spacing:.5px;text-transform:uppercase;padding:13px 30px;border-radius:30px;white-space:nowrap}

/* hero */
.hero{height:720px;background:var(--white)}
.hero-photo{position:absolute;inset:0;background:linear-gradient(100deg,#4f6b3a 0%,#7c9a5a 40%,#b9c79a 62%,#6f8a4c 80%,#3e5a2c 100%)}
.hero-curve{position:absolute;left:0;bottom:0;width:1200px;height:140px}
.topbar{position:absolute;top:0;left:0;right:0;height:70px;display:flex;align-items:center;padding:0 40px;color:var(--white)}
.brand{display:flex;align-items:center;gap:10px;font-size:26px;font-weight:600;color:var(--white)}
.brand-dot{width:34px;height:34px;border-radius:50%;background:var(--green)}
.contact-mini{display:flex;gap:36px;margin-left:auto;margin-right:30px;font-size:12px}
.contact-mini div{display:flex;align-items:center;gap:8px;line-height:1.3}
.contact-mini svg{width:28px;height:28px}
.contact-mini b{display:block;font-weight:600}
.mainnav{position:absolute;top:76px;right:40px;display:flex;gap:26px;font-size:12px;color:var(--white)}
.hero-copy{position:absolute;left:170px;top:320px;color:var(--white)}
.hero-copy h1{font-size:56px;line-height:1.05;font-weight:600;margin-bottom:34px}
.hero-copy h1 span{display:block}

/* features */
.features{height:300px;display:flex;justify-content:center;gap:36px}
.feature{width:220px;height:220px;border-radius:50%;background:var(--white);box-shadow:0 8px 28px rgba(0,0,0,.12);display:flex;flex-direction:column;align-items:center;justify-content:center;gap:14px;border:6px solid var(--white);outline:3px solid var(--green);outline-offset:-2px}
.feature svg{width:70px;height:70px}
.feature span{font-size:20px;font-weight:600}

/* about */
.about{height:540px}
.about-visual{position:absolute;left:160px;top:40px;width:420px;height:420px;border-radius:50%;background:radial-gradient(circle,#7fbf5a 0%,#3f7a2c 60%,#244a1d 100%);border:10px solid var(--white);box-shadow:0 0 0 6px var(--green)}
.about-copy{position:absolute;left:640px;top:110px;width:440px}
.about-copy h2{font-size:34px;line-height:1.2;font-weight:500;margin:8px 0 18px}
.about-copy h2 em{font-style:normal;color:var(--green);font-weight:600}
.about-copy p{font-size:13px;line-height:1.7;color:var(--muted);margin-bottom:22px}

/* photo band */
.band{height:520px}
.band-photo{position:absolute;inset:0;background:linear-gradient(180deg,#6b8a4e 0%,#9bb87a 45%,#5c8a3a 100%)}
.band svg{position:absolute;left:0;width:1200px}

/* video */
.video{height:480px;text-align:center}
.video .script{margin-top:50px}
.video h2{font-size:36px;font-weight:500;margin-top:2px}
.video h2 em{font-style:normal;color:var(--green);font-weight:600}
.video-frame{position:absolute;left:300px;top:150px;width:600px;height:320px;background:linear-gradient(180deg,#e9eef2 0%,#d3dde3 60%,#8fbf6f 100%);border-radius:4px}
.play{position:absolute;left:50%;top:46%;transform:translate(-50%,-50%);width:70px;height:70px}

/* best */
.best{height:240px}
.best h2{position:absolute;left:240px;top:60px;font-size:38px;font-weight:500;line-height:1.15}
.best h2 em{font-style:normal;color:var(--green);font-weight:600}
.best ul{position:absolute;left:680px;top:52px;list-style:none;font-size:14px}
.best li{display:flex;align-items:center;gap:10px;margin-bottom:8px}
.best li svg{width:16px;height:16px}
.best .btn{position:absolute;left:680px;top:178px}

/* testimonial */
.testimonial{height:640px;background:linear-gradient(180deg,var(--white) 0%,#f1f6ef 40%,#f1f6ef 100%)}
.testimonial .head{text-align:center;padding-top:60px}
.testimonial h2{font-size:40px;font-weight:500;line-height:1.2}
.testimonial h2 em{font-style:normal;color:var(--green);font-weight:600}
.person{position:absolute;left:130px;top:240px;width:230px;height:230px;border-radius:50%;background:linear-gradient(160deg,#c9d3cf,#7f9a8a);border:8px solid var(--white);box-shadow:0 0 0 4px var(--green)}
.quote-card{position:absolute;left:400px;top:230px;width:660px;height:250px;background:var(--white);border-radius:8px;box-shadow:0 10px 30px rgba(0,0,0,.08);padding:36px 50px}
.quote-card p{font-size:13px;line-height:1.75;color:var(--muted)}
.quote-card .who{margin-top:14px;font-size:13px;font-weight:600;color:var(--green)}
.quote-card .role{font-size:11px;color:var(--muted)}
.quote-mark{position:absolute;left:18px;top:18px;font-size:50px;color:var(--green);line-height:1}
.side-tabs{position:absolute;right:0;top:480px;display:flex;flex-direction:column;gap:4px}
.side-tabs i{display:block;width:44px;height:40px}

/* clients */
.clients{height:300px;text-align:center}
.clients-arc{position:absolute;left:0;top:60px;width:1200px;height:240px;background:var(--green-soft);border-radius:50% 50% 0 0/40% 40% 0 0}
.clients h2{position:relative;font-size:40px;font-weight:500;padding-top:100px}
.clients h2 em{font-style:normal;color:var(--green);font-weight:600}
.logo-row{position:absolute;left:130px;top:190px;display:flex;gap:22px;align-items:center}
.logo-row .tile{width:150px;height:74px;background:var(--white);display:flex;align-items:center;justify-content:center;font-weight:600;font-size:15px;color:var(--navy);box-shadow:0 4px 12px rgba(0,0,0,.06)}
.arrow{width:34px;height:34px;border-radius:50%;background:var(--green);display:flex;align-items:center;justify-content:center}

/* contact */
.contact{height:480px;background:linear-gradient(180deg,var(--green-soft) 0%,var(--green-soft) 55%,var(--navy) 55%,var(--navy) 100%)}
.contact-card{position:absolute;left:190px;top:30px;width:630px;height:420px;background:var(--green);border-radius:6px;color:var(--white);padding:36px 40px}
.contact-card h3{font-size:22px;font-weight:600}
.contact-card .lead{font-size:11px;opacity:.9;width:260px;margin:6px 0 26px}
.c-item{display:flex;gap:16px;align-items:center;margin-bottom:28px}
.c-item .ic{width:50px;height:50px;border-radius:50%;background:rgba(255,255,255,.2);display:flex;align-items:center;justify-content:center}
.c-item b{display:block;font-size:14px}
.c-item span{font-size:12px}
.form{position:absolute;left:700px;top:10px;width:310px;height:440px;background:var(--navy);border-radius:6px;padding:34px 30px;box-shadow:0 10px 30px rgba(0,0,0,.25)}
.form h3{color:var(--white);font-size:20px;font-weight:600;text-align:center;margin-bottom:22px}
.field{height:34px;background:var(--white);border-radius:3px;margin-bottom:12px;font-size:11px;color:#9aa3aa;padding:9px 12px}
.field.area{height:80px}

/* footer */
.footer{height:428px;background:var(--navy)}
.foot-brand{position:absolute;left:190px;top:60px}
.foot-brand .brand{font-size:24px}
.foot-brand p{font-size:11px;color:#9fb0bb;margin-top:8px}
.foot-col{position:absolute;top:60px;color:var(--white)}
.foot-col h4{font-size:14px;font-weight:600;margin-bottom:16px}
.foot-col li{list-style:none;font-size:12px;color:#b5c2ca;margin-bottom:10px}
.sub .input{display:block;width:150px;height:34px;background:var(--white);border-radius:17px;font-size:11px;color:#9aa3aa;padding:9px 14px}
.copy{position:absolute;left:0;right:0;bottom:0;height:56px;border-top:1px solid rgba(255,255,255,.12);text-align:center;font-size:11px;color:#9fb0bb;line-height:56px}
</style>
</head>
<body>

<header class="hero">
  <div class="hero-photo" role="img" aria-label="Woman enjoying fresh air on a balcony surrounded by green trees"></div>
  <svg class="hero-curve" viewBox="0 0 1200 140" preserveAspectRatio="none" aria-hidden="true">
    <path d="M0 60 Q600 200 1200 60 L1200 140 L0 140Z" fill="var(--green)" opacity=".9"/>
    <path d="M0 80 Q600 210 1200 80 L1200 140 L0 140Z" fill="#ffffff"/>
  </svg>
  <div class="topbar">
    <div class="brand"><i class="brand-dot"></i>Velmora</div>
    <div class="contact-mini">
      <div><svg viewBox="0 0 24 24"><circle cx="12" cy="12" r="12" fill="var(--green)"/><path d="M8 6l2 0 1 3-1.5 1a8 8 0 0 0 4.5 4.5l1-1.5 3 1 0 2a2 2 0 0 1-2 2A11 11 0 0 1 6 8a2 2 0 0 1 2-2z" fill="#fff"/></svg><span><b>Phone</b>+61 (0)2 5550 0148</span></div>
      <div><svg viewBox="0 0 24 24"><circle cx="12" cy="12" r="12" fill="var(--green)"/><rect x="6" y="8" width="12" height="8" rx="1" fill="#fff"/><path d="M6 8l6 5 6-5" stroke="var(--green)" fill="none"/></svg><span><b>Email</b>hello@velmora-sample.com.au</span></div>
    </div>
    <span class="btn">Request a Quote</span>
  </div>
  <nav class="mainnav"><span>Odour Control Products</span><span>How BioFiltration Works</span><span>Odour Control by Industry</span><span>Past Projects</span><span>About Us</span><span>Contact</span></nav>
  <div class="hero-copy">
    <h1><span>Odours</span><span>Controlled</span><span>Naturally</span></h1>
    <span class="btn">Request a Quote</span>
  </div>
</header>

<section class="features">
  <div class="feature"><svg viewBox="0 0 64 64" fill="none" stroke="var(--ink)" stroke-width="2.5"><path d="M8 20 32 8l24 12v26L32 58 8 46z"/><path d="M8 20l24 12 24-12M32 32v26"/><path d="M20 14l24 12" stroke="var(--green)"/></svg><span>Products</span></div>
  <div class="feature"><svg viewBox="0 0 64 64" fill="none" stroke="var(--ink)" stroke-width="2.5"><rect x="12" y="6" width="40" height="52" rx="3"/><path d="M20 20h4M20 32h4M20 44h4" stroke="var(--green)"/><path d="M30 20h14M30 32h14M30 44h14"/></svg><span>Features</span></div>
  <div class="feature"><svg viewBox="0 0 64 64" fill="none" stroke="var(--ink)" stroke-width="2.5"><path d="M6 16h20l5 6h27v32H6z"/><path d="M22 38l7 7 13-13" stroke="var(--green)"/></svg><span>Past Project</span></div>
</section>

<section class="about">
  <div class="about-visual" role="img" aria-label="Aerial view of a green forest with a recycling motif"></div>
  <div class="about-copy">
    <div class="script">About Us</div>
    <h2>Odour Control Solutions <em>About Velmora</em></h2>
    <p>Velmora uses sustainable biotechnology to resolve odour and corrosion problems in a highly efficient, environment friendly and cost effective manner. Our products, the Velmora series of biofilters, have been specifically engineered to overcome issues traditionally associated with biofiltration, such as bed compaction and uneven moisture levels, and our patented design achieves a removal rate of up to 99.9% per stage of treatment.</p>
    <span class="btn">Request a Quote</span>
  </div>
</section>

<section class="band">
  <div class="band-photo" role="img" aria-label="Smiling woman with arms outstretched in a sunlit forest"></div>
  <svg style="top:0;height:90px" viewBox="0 0 1200 90" preserveAspectRatio="none" aria-hidden="true"><path d="M0 0H1200V10Q600 120 0 10Z" fill="#fff"/></svg>
  <svg style="bottom:0;height:110px" viewBox="0 0 1200 110" preserveAspectRatio="none" aria-hidden="true"><path d="M0 110V40Q600 -30 1200 40V110Z" fill="#fff"/></svg>
</section>

<section class="video">
  <div class="script">Video</div>
  <h2>Watch <em>Video</em></h2>
  <div class="video-frame" role="img" aria-label="Video still showing a treatment plant with trees and eco icons">
    <svg class="play" viewBox="0 0 70 70"><circle cx="35" cy="35" r="33" fill="var(--green)" stroke="#fff" stroke-width="4"/><path d="M28 22l20 13-20 13z" fill="#fff"/></svg>
  </div>
</section>

<section class="best">
  <h2>What makes us<br><em>the best?</em></h2>
  <ul>
    <li><svg viewBox="0 0 16 16"><circle cx="8" cy="8" r="8" fill="var(--green)"/><path d="M4.5 8l2.5 2.5 4.5-5" stroke="#fff" stroke-width="1.8" fill="none"/></svg>Biological &amp; Sustainable technology</li>
    <li><svg viewBox="0 0 16 16"><circle cx="8" cy="8" r="8" fill="var(--green)"/><path d="M4.5 8l2.5 2.5 4.5-5" stroke="#fff" stroke-width="1.8" fill="none"/></svg>Efficient maintenance cost</li>
    <li><svg viewBox="0 0 16 16"><circle cx="8" cy="8" r="8" fill="var(--green)"/><path d="M4.5 8l2.5 2.5 4.5-5" stroke="#fff" stroke-width="1.8" fill="none"/></svg>100% Australian Owned</li>
    <li><svg viewBox="0 0 16 16"><circle cx="8" cy="8" r="8" fill="var(--green)"/><path d="M4.5 8l2.5 2.5 4.5-5" stroke="#fff" stroke-width="1.8" fill="none"/></svg>Eco Friendly</li>
  </ul>
  <span class="btn">Request a Quote</span>
</section>

<section class="testimonial">
  <div class="head">
    <div class="script">Testimonials</div>
    <h2>As soon as the system was started,<br><em>the smell disappeared!</em></h2>
  </div>
  <div class="person" role="img" aria-label="Portrait of a satisfied client"></div>
  <div class="quote-card">
    <span class="quote-mark">“</span>
    <p>Year and the Velmora team promised to stop the odour from our smelly neighbour and they delivered. In addition, as soon as the system was started, the smell disappeared. The system is well designed, very professionally installed and the beauty of it is, apart from a constantly running fan, it is bacteria doing the heavy lifting, so it is very environmentally friendly. We lived with the smell for 3 years which could be extremely frustrating and unpleasant. Now the problem is solved and we can have BBQs again. We are happy and our neighbours have noticed the odour is gone. Thank you!</p>
    <div class="who">Reid Calloway</div>
    <div class="role">Resident next to a municipal wastewater pump station</div>
  </div>
  <div class="side-tabs" aria-hidden="true"><i style="background:var(--navy)"></i><i style="background:var(--navy)"></i><i style="background:var(--green)"></i></div>
</section>

<section class="clients">
  <div class="clients-arc"></div>
  <h2>Our Happy <em>Clients</em></h2>
  <div class="logo-row">
    <span class="arrow"><svg width="12" height="12" viewBox="0 0 12 12"><path d="M8 1 3 6l5 5" stroke="#fff" stroke-width="2" fill="none"/></svg></span>
    <div class="tile">Lumbrook</div>
    <div class="tile">Corvane</div>
    <div class="tile">Tessaly</div>
    <div class="tile">Norwyn</div>
    <div class="tile">Hallowmere</div>
    <span class="arrow"><svg width="12" height="12" viewBox="0 0 12 12"><path d="M4 1l5 5-5 5" stroke="#fff" stroke-width="2" fill="none"/></svg></span>
  </div>
</section>

<section class="contact">
  <div class="contact-card">
    <h3>CONTACT US</h3>
    <p class="lead">If you have queries regarding our products, please let us know and we will contact you.</p>
    <div class="c-item"><span class="ic"><svg width="22" height="22" viewBox="0 0 24 24"><path d="M12 2a7 7 0 0 0-7 7c0 5 7 13 7 13s7-8 7-13a7 7 0 0 0-7-7zm0 9.5A2.5 2.5 0 1 1 12 6.5a2.5 2.5 0 0 1 0 5z" fill="#fff"/></svg></span><div><b>Location</b><span>18 Fernbrook Way, Lakeside<br>NSW 2000, Australia</span></div></div>
    <div class="c-item"><span class="ic"><svg width="22" height="22" viewBox="0 0 24 24"><rect x="3" y="6" width="18" height="12" rx="1" fill="#fff"/><path d="M3 6l9 7 9-7" stroke="var(--green)" fill="none" stroke-width="1.5"/></svg></span><div><b>Email Address</b><span>hello@velmora-sample.com.au</span></div></div>
    <div class="c-item"><span class="ic"><svg width="22" height="22" viewBox="0 0 24 24"><path d="M6 3h3l1.5 4.5L8.5 9a11 11 0 0 0 6.5 6.5l1.5-2 4.5 1.5v3a2 2 0 0 1-2 2A17 17 0 0 1 4 5a2 2 0 0 1 2-2z" fill="#fff"/></svg></span><div><b>Phone Number</b><span>+61 (0)2 5550 0148</span></div></div>
  </div>
  <div class="form">
    <h3>SEND US A MESSAGE</h3>
    <div class="field">First Name*</div>
    <div class="field">Last Name*</div>
    <div class="field">Email*</div>
    <div class="field">Subject*</div>
    <div class="field area">Your message here*</div>
    <span class="btn" style="padding:10px 24px;font-size:10px">Submit Now</span>
  </div>
</section>

<footer class="footer">
  <div class="foot-brand"><div class="brand"><i class="brand-dot"></i>Velmora</div><p>Natural odour control solutions</p></div>
  <div class="foot-col" style="left:430px"><h4>QUICK LINKS</h4><ul><li>Odour Control Products</li><li>How BioFiltration Works</li><li>Odour Control by Industry</li><li>Past Projects</li><li>About Us</li></ul></div>
  <div class="foot-col" style="left:640px"><h4>OTHER LINKS</h4><ul><li>Privacy Policy</li><li>Sitemap</li></ul></div>
  <div class="foot-col" style="left:800px"><h4>CONTACT INFO</h4><div class="sub"><span class="input">Enter email</span></div><span class="btn" style="padding:9px 18px;font-size:10px;margin-top:10px">Subscribe Now</span></div>
  <div class="copy">Copyright © 2024 Velmora · All Rights Reserved</div>
</footer>

</body>
</html>
```